Marlowe Ridge Holdings

I have a real estate investment business.

** I need editable vector files of the final design.

Industry/Entity Type

Real Estate

Contact Information for Business Card

I would like the card to be clear and direct with the company name and contact info. I would prefer not to have a design that is too busy (i.e., with excessive detail) in the business card.

Font styles to use
Sans Serif

Requirements
Must have
• My card must have the following information listed below:
• Company name: Marlowe Ridge Holdings LLC
• My name: Daniel Vestrap
• Phone number: (555) 218-9064
• Email address: dlvestrap@fernmail.example
• Keywords: “Real Estate Investments”
Nice to have
• I would like to have a design that resembles the characteristics/uses of obsidian stone which resembles something related to strength and resilience. Perhaps something with sharp, sleek color transitions as well.

```html
<!DOCTYPE html>
<html lang="en">
<head>
<meta charset="utf-8">
<title>Marlowe Ridge Holdings LLC – Business Card</title>
<link rel="stylesheet" href="https://fonts.googleapis.com/css2?family=Cinzel:wght@500;600&family=Arimo:wght@400&display=swap">
<style>
  :root {
    --backdrop: #cfcdcd;
    --paper: #f1f5f6;
    --steel-blue: #0f5684;
    --obsidian: #03273f;
    --ink: #0a2a44;
    --white: #ffffff;
  }
  html, body {
    margin: 0;
    width: 1200px;
    height: 1200px;
    overflow: hidden;
    background: var(--backdrop);
  }
  .business-card {
    position: absolute;
    left: 100px;
    top: 314px;
    width: 1000px;
    height: 572px;
    background: var(--paper);
    overflow: hidden;
    box-shadow: 0 18px 40px rgba(0,0,0,0.18);
  }
  .band { position: absolute; left: 0; width: 100%; }
  .band--upper-accent { top: 190px; height: 50px; background: var(--steel-blue); }
  .band--obsidian { top: 240px; height: 250px; background: var(--obsidian); }
  .band--lower-accent { top: 490px; height: 82px; background: var(--steel-blue); }

  .company {
    position: absolute;
    top: 58px;
    left: 0;
    width: 100%;
    text-align: center;
    color: var(--ink);
    font-family: "Cinzel", serif;
  }
  .company__name {
    margin: 0;
    font-size: 44px;
    font-weight: 600;
    letter-spacing: 1px;
    line-height: 1;
  }
  .company__tagline {
    margin: 8px 0 0;
    font-size: 26px;
    font-weight: 500;
    letter-spacing: 1px;
    line-height: 1;
  }

  .contact-line {
    position: absolute;
    left: 0;
    top: 240px;
    width: 1000px;
    height: 250px;
  }
  .holder-name {
    position: absolute;
    left: 345px;
    top: 92px;
    margin: 0;
    color: var(--white);
    font-family: "Arimo", sans-serif;
    font-size: 48px;
    font-weight: 400;
    line-height: 1;
    white-space: nowrap;
  }
  .contact-detail {
    position: absolute;
    top: 184px;
    margin: 0;
    color: var(--white);
    font-family: "Arimo", sans-serif;
    font-size: 24px;
    line-height: 1;
    white-space: nowrap;
  }
  .contact-detail--phone { left: 88px; }
  .contact-detail--email { right: 60px; }
</style>
</head>
<body>
  <article class="business-card">
    <div class="band band--upper-accent"></div>
    <div class="band band--obsidian"></div>
    <div class="band band--lower-accent"></div>

    <header class="company">
      <h1 class="company__name">Marlowe Ridge Holdings LLC</h1>
      <p class="company__tagline">“Real Estate Investments”</p>
    </header>

    <section class="contact-line">
      <svg class="connectors" width="1000" height="250" viewBox="0 0 1000 250" aria-hidden="true">
        <!-- phone badge -->
        <g class="badge badge--phone" fill="none" stroke="#ffffff">
          <path d="M 206 108 A 58 58 0 1 0 206 132" stroke-width="9"/>
          <circle cx="150" cy="120" r="40" fill="#ffffff" stroke="none"/>
          <g fill="#03273f" stroke="none">
            <path d="M126 112 q24 -18 48 0 l-5 8 h-8 l-2 -6 q-9 -3 -18 0 l-2 6 h-8 z"/>
            <rect x="134" y="119" width="32" height="20" rx="3"/>
          </g>
          <circle cx="150" cy="129" r="5" fill="#ffffff" stroke="none"/>
          <line x1="206" y1="120" x2="330" y2="120" stroke-width="8"/>
          <line x1="330" y1="100" x2="330" y2="140" stroke-width="8"/>
        </g>
        <!-- email badge -->
        <g class="badge badge--email" fill="none" stroke="#ffffff">
          <line x1="706" y1="100" x2="706" y2="140" stroke-width="8"/>
          <line x1="706" y1="120" x2="792" y2="120" stroke-width="8"/>
          <path d="M 794 108 A 58 58 0 1 1 794 132" stroke-width="9"/>
          <circle cx="850" cy="120" r="40" fill="#ffffff" stroke="none"/>
          <rect x="828" y="106" width="44" height="30" fill="#03273f" stroke="none"/>
          <path d="M830 108 L850 124 L870 108" stroke="#ffffff" stroke-width="3"/>
          <circle cx="850" cy="110" r="5" stroke="#ffffff" stroke-width="2"/>
        </g>
      </svg>
      <p class="holder-name">Daniel Vestrap</p>
      <p class="contact-detail contact-detail--phone">(555) 218-9064</p>
      <p class="contact-detail contact-detail--email">dlvestrap@fernmail.example</p>
    </section>
  </article>
</body>
</html>
```